VELINTA Promotions - Business Card Design Project

We are looking for a classy business cards for Promotion Company based in Toronto, Canada named Velinta Promotions.

Velinta Promotions has an idea and vision to set high standard, be EXCLUSIVE and attract a group of people that will follow us through events we promote (night clubs, brand promotions, music events, and sport events)

We want to present a high standards and classy image to the others...
Updates

Target Market(s)

male/female age 25-40 Target: business owners young entrepreneur - clubing industry - media industry - promotion industry - marketing media industry

Industry/Entity Type

Events

Requirements
Must have
• business cards should be classy, make people feel exclusive , make people react ..

```html
<!DOCTYPE html>
<html lang="en">
<head>
<meta charset="utf-8">
<title>Velinta Promotions – Business Card</title>
<link rel="stylesheet" href="https://fonts.googleapis.com/css2?family=PT+Sans+Narrow&family=Source+Sans+3:wght@400;700&display=swap">
<style>
  :root {
    --card-white: #ffffff;
    --brand-cyan: #48fcff;
    --brand-cyan-deep: #3ee6ee;
    --ink: #111111;
    --on-cyan: #ffffff;
  }
  html, body {
    margin: 0;
    padding: 0;
    overflow: hidden;
    background: var(--card-white);
  }
  .card {
    position: relative;
    width: 751px;
    height: 1200px;
    background: var(--card-white);
    overflow: hidden;
  }
  .card-art {
    position: absolute;
    inset: 0;
  }
  .cyan-band { fill: var(--brand-cyan); }
  .identity {
    position: absolute;
    top: 72px;
    right: 423px;
    text-align: right;
    color: var(--ink);
    font-family: "Source Sans 3", sans-serif;
  }
  .identity-name {
    margin: 0;
    font-size: 47px;
    font-weight: 700;
    letter-spacing: -0.5px;
    line-height: 1.1;
  }
  .identity-role {
    margin: 8px 0 0;
    font-size: 44px;
    font-weight: 400;
    line-height: 1.05;
  }
  .identity-email,
  .identity-phone {
    margin: 0;
    font-family: "PT Sans Narrow", sans-serif;
    font-size: 31px;
    line-height: 1.4;
  }
  .brand-name {
    font-family: "Source Sans 3", sans-serif;
    font-weight: 400;
    fill: var(--brand-cyan-deep);
  }
  .brand-word { font-size: 150px; letter-spacing: 4px; }
  .brand-sub { font-size: 34px; letter-spacing: 14px; }
  .company-contact {
    font-family: "PT Sans Narrow", sans-serif;
    font-size: 50px;
    fill: var(--on-cyan);
  }
</style>
</head>
<body>
  <main class="card">
    <svg class="card-art" width="751" height="1200" viewBox="0 0 751 1200" aria-hidden="false">
      <path class="cyan-band" d="M647 0 H751 V1150 Q751 1200 701 1200 H63 Z"/>

      <g class="brand-name" aria-label="Velinta Promotions">
        <text class="brand-word" transform="translate(85 926) rotate(-64)">VELINTA</text>
        <text class="brand-sub" transform="translate(148 957) rotate(-64)">PROMOTIONS</text>
      </g>

      <text class="company-contact" transform="translate(235 1016) rotate(-63)">
        <tspan x="0" dy="0">48 St. .......................</tspan>
        <tspan x="0" dy="70">Toronto - CANADA</tspan>
        <tspan x="0" dy="70">T. 224781305 • F. 22491738 •</tspan>
        <tspan x="0" dy="70">w. www.velinta.com</tspan>
      </text>
    </svg>

    <section class="identity">
      <h1 class="identity-name">Dana HOLT</h1>
      <p class="identity-role">Director</p>
      <p class="identity-email">d.holt@velinta.com</p>
      <p class="identity-phone">058417293</p>
    </section>
  </main>
</body>
</html>
```